Step and Repeat Backdrop for wedding reception photo booth

Would like to have a Step and Repeat Backdrop (8 foot high by 10 foot wide) that incorporates the wedding logo (attached) and the names Elena and Gavin. Background should be white, and wedding colors are burgundy and gold. Show me creativity :-) I have included some random samples.

```html
<!DOCTYPE html>
<html lang="en">
<head>
<meta charset="utf-8">
<title>Elena &amp; Gavin — Step and Repeat Backdrop</title>
<link rel="stylesheet" href="https://fonts.googleapis.com/css2?family=Pinyon+Script&display=swap">
<style>
  :root {
    --paper: #ffffff;
    --burgundy: #4e0f22;
    --ink: #111111;
    --gold: #b8955a;
  }
  html, body {
    margin: 0;
    padding: 0;
    overflow: hidden;
    background: var(--paper);
  }
  .backdrop {
    position: relative;
    width: 960px;
    height: 1200px;
    background: var(--paper);
    overflow: hidden;
    font-family: "Pinyon Script", cursive;
  }
  .names,
  .monogram {
    position: absolute;
    transform: translate(-50%, -50%);
    white-space: nowrap;
    line-height: 1;
    margin: 0;
  }
  .names {
    font-size: 44px;
    color: var(--burgundy);
  }
  .names--ink {
    color: var(--ink);
  }
  .names .amp {
    font-size: 26px;
    padding: 0 6px;
    vertical-align: 4px;
  }
  .monogram {
    font-size: 46px;
    color: var(--gold);
  }
  .monogram--hero {
    font-size: 128px;
  }
</style>
</head>
<body>
<main class="backdrop" aria-label="Elena and Gavin wedding step and repeat backdrop">

  <!-- Row 1 -->
  <p class="monogram" style="left:123px; top:123px;">E&amp;G</p>
  <p class="names" style="left:361px; top:123px;">Elena<span class="amp">&amp;</span>Gavin</p>
  <p class="monogram" style="left:599px; top:123px;">E&amp;G</p>
  <p class="names names--ink" style="left:816px; top:117px;">Elena<span class="amp">&amp;</span>Gavin</p>

  <!-- Row 2 -->
  <p class="names" style="left:164px; top:261px;">Elena<span class="amp">&amp;</span>Gavin</p>
  <p class="monogram" style="left:392px; top:263px;">E&amp;G</p>
  <p class="names" style="left:641px; top:261px;">Elena<span class="amp">&amp;</span>Gavin</p>
  <p class="monogram" style="left:844px; top:261px;">E&amp;G</p>

  <!-- Row 3 -->
  <p class="monogram" style="left:129px; top:399px;">E&amp;G</p>
  <p class="names" style="left:361px; top:401px;">Elena<span class="amp">&amp;</span>Gavin</p>
  <p class="monogram" style="left:604px; top:399px;">E&amp;G</p>
  <p class="names" style="left:816px; top:393px;">Elena<span class="amp">&amp;</span>Gavin</p>

  <!-- Centre row -->
  <p class="names" style="left:177px; top:611px;">Elena<span class="amp">&amp;</span>Gavin</p>
  <p class="monogram monogram--hero" style="left:479px; top:600px;">E&amp;G</p>
  <p class="names" style="left:793px; top:611px;">Elena<span class="amp">&amp;</span>Gavin</p>

  <!-- Row 5 -->
  <p class="monogram" style="left:123px; top:775px;">E&amp;G</p>
  <p class="names" style="left:361px; top:775px;">Elena<span class="amp">&amp;</span>Gavin</p>
  <p class="monogram" style="left:599px; top:775px;">E&amp;G</p>
  <p class="names names--ink" style="left:816px; top:769px;">Elena<span class="amp">&amp;</span>Gavin</p>

  <!-- Row 6 -->
  <p class="names" style="left:164px; top:913px;">Elena<span class="amp">&amp;</span>Gavin</p>
  <p class="monogram" style="left:392px; top:915px;">E&amp;G</p>
  <p class="names" style="left:641px; top:913px;">Elena<span class="amp">&amp;</span>Gavin</p>
  <p class="monogram" style="left:844px; top:913px;">E&amp;G</p>

  <!-- Row 7 -->
  <p class="monogram" style="left:129px; top:1050px;">E&amp;G</p>
  <p class="names" style="left:361px; top:1052px;">Elena<span class="amp">&amp;</span>Gavin</p>
  <p class="monogram" style="left:604px; top:1050px;">E&amp;G</p>
  <p class="names" style="left:816px; top:1045px;">Elena<span class="amp">&amp;</span>Gavin</p>

</main>
</body>
</html>
```